Profi-Kistenhof
Zielgruppe
Profi-Kistenhof.de vermietet Lagercontainern an Privatkunden und Gewerbetriebende
Vermietung von Stellfächen für Wohnmobile/Boote etc
Das ganze auf einem Gewerbegelände in Köln (Brauweiler)
Aufgabenstellung
Erstellung eines 2-Seitigen DIN lang (10,5 x 21 cm) Flyers
Seite A: Vermietung von Lagercontainern
Seite B: Stellfächen für Wohnmobile/Boote
Wichtig: Die Sicherheit (Zutrittskontrolle, Videoüberwachung, Brandmeldeanlage)
Preise sollen auf Flyern erscheinen, diese wie auch die Textee möchte ich jedoch ändern können.
Alle Texte können auch von der Seite profi-kistenhof.de übernommen werden
Das Logo (siehe boxen_welten.ai) müsste noch bearbeitet werden .... also "boxenwelten" raus und dafür "PROFI-KISTENHOF" rein
Gerne mit Symbolen arbeiten ..

```html
<!DOCTYPE html>
<html lang="de">
<head>
<meta charset="utf-8">
<title>Profi-Kistenhof – Flyer</title>
<link rel="stylesheet" href="https://fonts.googleapis.com/css2?family=Ubuntu:wght@400;500;700&display=swap">
<style>
  :root{
    --navy:#1c2b45;
    --green:#17703a;
    --green-light:#e6f0ea;
    --blue:#1a69b0;
    --blue-light:#e4eff8;
    --grey-top:#ffffff;
    --grey-bottom:#d6d6d6;
    --white:#ffffff;
  }
  *{box-sizing:border-box;margin:0;padding:0}
  html,body{width:1200px;height:952px;overflow:hidden;background:var(--white)}
  body{position:relative;font-family:"Ubuntu",Arial,sans-serif}
  .flyer{position:absolute;top:61px;width:404px;height:791px;overflow:hidden}
  .flyer--storage{left:85px;--accent:var(--green);--accent-light:var(--green-light)}
  .flyer--parking{left:677px;--accent:var(--blue);--accent-light:var(--blue-light)}
  .flyer__head{position:absolute;left:0;top:0;width:100%;height:310px;
    background:linear-gradient(to bottom,var(--grey-top) 0%,var(--grey-top) 25%,var(--grey-bottom) 100%)}
  .brand{position:absolute;left:21px;top:7px;width:360px;height:103px;background:var(--navy);
    border-radius:8px;box-shadow:inset 0 0 0 3px var(--navy),inset 0 0 0 5px var(--white);
    display:flex;align-items:center;gap:16px;padding-left:26px}
  .brand__square{width:44px;height:44px;background:var(--white);border-radius:4px}
  .brand__name{color:var(--white);font-weight:500;font-size:27px;letter-spacing:1px}
  .contact{position:absolute;left:24px;top:124px;color:var(--navy)}
  .contact__web{font-size:18px;font-weight:700}
  .contact__line{font-size:12px;margin-top:5px}
  .contact__line + .contact__line{margin-top:3px}
  .photo{position:absolute}
  .photo--container{left:212px;top:130px;width:142px;height:129px;
    background:linear-gradient(135deg,#2d3a7c 0%,#3c4a94 50%,#9aa0a8 100%);border-radius:3px}
  .photo--camper{left:197px;top:123px;width:171px;height:118px;
    background:linear-gradient(180deg,#f4f4f4 0%,#e2e4e6 60%,#6a6f75 100%);border-radius:14px 30px 10px 10px}
  .headline{position:absolute;left:24px;top:226px;color:var(--accent);font-size:28px;font-weight:500;line-height:34px}
  .flyer__body{position:absolute;left:0;top:310px;width:100%;height:481px;background:var(--accent);color:var(--white)}
  .intro{position:absolute;left:29px;top:17px;font-size:12.5px;line-height:15px}
  .features{position:absolute;left:32px;top:99px;list-style:none}
  .features li{display:flex;align-items:center;height:30.7px;font-size:16.5px}
  .features svg{width:13px;height:13px;margin-right:8px}
  .symbol{position:absolute}
  .symbol--boxes{left:283px;top:172px}
  .symbol--camper{left:296px;top:172px}
  .price{position:absolute;left:27px;top:271px;width:349px;height:115px;background:var(--accent-light);
    color:var(--accent);padding:12px 14px}
  .price__amount{font-size:18px;font-weight:700}
  .price__offer{font-size:12.5px;margin-top:10px}
  .price__note{font-size:7.5px;line-height:10px;margin-top:10px}
  .claims{position:absolute;left:28px;top:415px;display:flex;gap:18px;font-size:25px;font-weight:500}
  .claims span{display:flex;align-items:center}
  .claims svg{width:15px;height:15px;margin-right:5px}
</style>
</head>
<body>

<section class="flyer flyer--storage">
  <header class="flyer__head">
    <div class="brand"><span class="brand__square"></span><span class="brand__name">PROFI-KISTENHOF</span></div>
    <div class="contact">
      <p class="contact__web">Profi-Kistenhof.de</p>
      <p class="contact__line">Tel.:&nbsp; 02234 5550187</p>
      <p class="contact__line">ft@profi-kistenhof.de</p>
    </div>
    <div class="photo photo--container" role="img" aria-label="Foto: offener blauer Lagercontainer mit Kartons"></div>
    <h1 class="headline">Vermietung<br>von Lagercontainern</h1>
  </header>
  <div class="flyer__body">
    <p class="intro">Profi-Kistenhof vermietet Container<br>zu kleinem Preis und Top-Konditionen<br>für die Lagerung privater oder gewerblicher Güter -<br>auch als kurzfristige Lösung (z.B. bei Umzug) geeignet.</p>
    <ul class="features">
      <li><svg viewBox="0 0 12 12"><path d="M1.5 6.5l3 3 6-7" fill="none" stroke="#fff" stroke-width="2"/></svg>Rund um die Uhr zugänglich</li>
      <li><svg viewBox="0 0 12 12"><path d="M1.5 6.5l3 3 6-7" fill="none" stroke="#fff" stroke-width="2"/></svg>14m² bzw. 33m³ Kapazität</li>
      <li><svg viewBox="0 0 12 12"><path d="M1.5 6.5l3 3 6-7" fill="none" stroke="#fff" stroke-width="2"/></svg>Zutrittskontrolle</li>
      <li><svg viewBox="0 0 12 12"><path d="M1.5 6.5l3 3 6-7" fill="none" stroke="#fff" stroke-width="2"/></svg>Videoüberwacht</li>
      <li><svg viewBox="0 0 12 12"><path d="M1.5 6.5l3 3 6-7" fill="none" stroke="#fff" stroke-width="2"/></svg>14 Tage Kündigungsfrist</li>
    </ul>
    <svg class="symbol symbol--boxes" width="82" height="64" viewBox="0 0 82 64">
      <g fill="#fff" stroke="#17703a" stroke-width="1.5">
        <rect x="14" y="2" width="28" height="28"/>
        <rect x="1" y="30" width="28" height="32"/>
        <rect x="29" y="30" width="28" height="32"/>
        <rect x="57" y="30" width="24" height="32"/>
      </g>
    </svg>
    <div class="price">
      <p class="price__amount">148,- € pro Monat*</p>
      <p class="price__offer">1 Monat gratis bei einer Anmietung ab 3 Monaten</p>
      <p class="price__note">* Preis gilt pro Monat und Container für private Vermietung,<br>bei gewerblicher Anmietung zzgl. 19% MwSt.</p>
    </div>
    <div class="claims">
      <span><svg viewBox="0 0 12 12"><path d="M1.5 6.5l3 3 6-7" fill="none" stroke="#fff" stroke-width="2"/></svg>günstig</span>
      <span><svg viewBox="0 0 12 12"><path d="M1.5 6.5l3 3 6-7" fill="none" stroke="#fff" stroke-width="2"/></svg>sicher</span>
      <span><svg viewBox="0 0 12 12"><path d="M1.5 6.5l3 3 6-7" fill="none" stroke="#fff" stroke-width="2"/></svg>lagern</span>
    </div>
  </div>
</section>

<section class="flyer flyer--parking">
  <header class="flyer__head">
    <div class="brand"><span class="brand__square"></span><span class="brand__name">PROFI-KISTENHOF</span></div>
    <div class="contact">
      <p class="contact__web">Profi-Kistenhof.de</p>
      <p class="contact__line">Tel.:&nbsp; 02234 5550187</p>
      <p class="contact__line">ft@profi-kistenhof.de</p>
    </div>
    <div class="photo photo--camper" role="img" aria-label="Foto: weißes Wohnmobil in Seitenansicht"></div>
    <h1 class="headline">Stellfächen für<br>Wohnmobile/Boote</h1>
  </header>
  <div class="flyer__body">
    <p class="intro">Profi-Kistenhof vermietet Stellflächen für Wohnmobile<br>oder Boote&nbsp; zu kleinem Preis und Top-Konditionen<br>&nbsp;- auch als kurzfristige Lösung (z.B. bei Umzug) geeignet.</p>
    <ul class="features">
      <li><svg viewBox="0 0 12 12"><path d="M1.5 6.5l3 3 6-7" fill="none" stroke="#fff" stroke-width="2"/></svg>Rund um die Uhr zugänglich</li>
      <li><svg viewBox="0 0 12 12"><path d="M1.5 6.5l3 3 6-7" fill="none" stroke="#fff" stroke-width="2"/></svg>Zutrittskontrolle</li>
      <li><svg viewBox="0 0 12 12"><path d="M1.5 6.5l3 3 6-7" fill="none" stroke="#fff" stroke-width="2"/></svg>Videoüberwacht</li>
      <li><svg viewBox="0 0 12 12"><path d="M1.5 6.5l3 3 6-7" fill="none" stroke="#fff" stroke-width="2"/></svg>Brandmeldeanlage</li>
      <li><svg viewBox="0 0 12 12"><path d="M1.5 6.5l3 3 6-7" fill="none" stroke="#fff" stroke-width="2"/></svg>14 Tage Kündigungsfrist</li>
    </ul>
    <svg class="symbol symbol--camper" width="78" height="78" viewBox="0 0 78 78">
      <rect x="1.5" y="1.5" width="75" height="75" rx="4" fill="#fff" stroke="#000" stroke-width="3"/>
      <rect x="6" y="6" width="66" height="66" rx="2" fill="#000"/>
      <path d="M12 26h46l8 12v14H12z" fill="#fff"/>
      <rect x="18" y="31" width="12" height="8" fill="#000"/>
      <rect x="50" y="31" width="8" height="7" fill="#000"/>
      <circle cx="24" cy="54" r="6" fill="#fff" stroke="#000" stroke-width="2"/>
      <circle cx="54" cy="54" r="6" fill="#fff" stroke="#000" stroke-width="2"/>
    </svg>
    <div class="price">
      <p class="price__amount">148,- € pro Monat*</p>
      <p class="price__offer">1 Monat gratis bei einer Anmietung ab 3 Monaten</p>
      <p class="price__note">* Preis gilt pro Monat und Container für private Vermietung,<br>bei gewerblicher Anmietung zzgl. 19% MwSt.</p>
    </div>
    <div class="claims">
      <span><svg viewBox="0 0 12 12"><path d="M1.5 6.5l3 3 6-7" fill="none" stroke="#fff" stroke-width="2"/></svg>günstig</span>
      <span><svg viewBox="0 0 12 12"><path d="M1.5 6.5l3 3 6-7" fill="none" stroke="#fff" stroke-width="2"/></svg>sicher</span>
      <span><svg viewBox="0 0 12 12"><path d="M1.5 6.5l3 3 6-7" fill="none" stroke="#fff" stroke-width="2"/></svg>parken</span>
    </div>
  </div>
</section>

</body>
</html>
```